Rural contractor needs professional informative business card

We need a business card design that looks professional but also includes information about the services that the business offers.
The business is an earthmoving and transport business. All of the services offered are listed on the old card attached.
The business is aimed at farmers so the design we are after is a classic look. The card needs to include all of the information that is listed on the old card design uploaded as an attachment. We recognize that this is a lot of information to fit on a business card but it also operates as a key marketing tool so is very important to the business.
Feel free to send me your questions.
Thanks
Reason: We are having trouble deciding between all these great designs - thank you for your efforts
We would love to see some designs using red with a little white and black. Also feel free to re-design our logo if you feel it needs to be to fit your designs. Thank you

```html
<!DOCTYPE html>
<html lang="en">
<head>
<meta charset="utf-8">
<title>CR Reardon Contracting – Business Card</title>
<link rel="stylesheet" href="https://fonts.googleapis.com/css2?family=Roboto+Condensed:ital,wght@0,400;0,700;1,400&family=Oswald:wght@600&display=swap">
<style>
  :root {
    --yellow-light: #ffe61c;
    --yellow-deep: #f8b41e;
    --ink: #2b2b2b;
    --tread: #7a7b7e;
    --tread-dark: #5f6063;
    --white: #ffffff;
    --heading-yellow: #f7c51a;
    --page: #ffffff;
  }
  * { margin: 0; padding: 0; box-sizing: border-box; }
  html, body { width: 1015px; height: 1200px; overflow: hidden; background: var(--page); }
  body { position: relative; font-family: "Roboto Condensed", "Arial Narrow", sans-serif; color: var(--ink); }

  .card {
    position: absolute; left: 25px; width: 965px; height: 548px;
    border-radius: 30px; overflow: hidden;
    box-shadow: 0 3px 10px rgba(0,0,0,0.25);
  }
  .card--front { top: 20px; background: linear-gradient(60deg, var(--yellow-deep) 0%, var(--yellow-light) 55%, var(--yellow-light) 100%); }
  .card--back { top: 632px; }

  /* front */
  .brand { position: absolute; left: 36px; top: 38px; width: 446px; text-align: center; }
  .brand__rule { height: 3px; background: var(--ink); }
  .brand__name { font-size: 62px; font-weight: 700; line-height: 68px; color: var(--ink); }
  .brand__tag { font-size: 27px; font-weight: 700; letter-spacing: 15px; color: var(--ink); margin-top: 10px; padding-left: 14px; }

  .person {
    position: absolute; left: 48px; top: 192px;
    font-family: "Oswald", "Roboto Condensed", sans-serif; font-weight: 600; font-size: 42px;
    color: var(--white);
    text-shadow: -2px 0 var(--ink), 2px 0 var(--ink), 0 -2px var(--ink), 0 2px var(--ink), 2px 2px var(--ink), -2px -2px var(--ink), 2px -2px var(--ink), -2px 2px var(--ink);
  }
  .contact { position: absolute; left: 44px; top: 256px; list-style: none; font-size: 29px; line-height: 37.5px; }
  .contact li { display: flex; align-items: flex-start; }
  .contact svg { width: 28px; height: 28px; margin-top: 5px; margin-right: 2px; flex: none; }
  .contact .indent { padding-left: 48px; }

  .hero-photo {
    position: absolute; left: 580px; top: 43px; width: 344px; height: 255px;
    border: 3px solid var(--ink); border-radius: 14px;
    background: linear-gradient(180deg, #5f8fd6 0%, #9dbde6 40%, #d9c59a 62%, #c7a36d 100%);
  }
  .hero-caption { position: absolute; left: 580px; top: 303px; width: 344px; text-align: center; font-size: 31px; font-weight: 700; }

  .tread { position: absolute; left: 0; width: 100%; background: var(--tread); }
  .tread--front { top: 425px; height: 86px; }

  /* back */
  .back-photo {
    position: absolute; inset: 0;
    background: linear-gradient(180deg, #8e8e8e 0%, #bdbdbd 40%, #d8d8d8 58%, #6f6f6f 66%, #b5b5b5 74%, #cfcfcf 100%);
  }
  .tread--top { top: 0; height: 60px; background: var(--tread-dark); }
  .tread--bottom { bottom: 0; height: 56px; background: var(--tread); }

  .services { position: absolute; top: 18px; text-align: center; color: var(--white); }
  .services--earth { left: 138px; width: 340px; }
  .services--transport { left: 613px; width: 280px; }
  .services h2 { font-size: 32px; font-weight: 700; color: var(--heading-yellow); line-height: 42px; margin-bottom: 6px; }
  .services ul { list-style: none; font-style: italic; font-size: 27px; line-height: 32.5px; }
</style>
</head>
<body>

<section class="card card--front">
  <div class="brand">
    <div class="brand__rule"></div>
    <div class="brand__name">CR Reardon</div>
    <div class="brand__rule"></div>
    <div class="brand__tag">CONTRACTING</div>
  </div>

  <div class="person">Callum Reardon</div>

  <ul class="contact">
    <li>
      <svg viewBox="0 0 28 28"><path d="M6 4c2-1 4 2 5 4 1 2-1 3-1 4 1 3 3 5 6 6 1 0 2-2 4-1 2 1 5 3 4 5-1 2-3 3-5 3C11 24 4 17 4 8c0-2 1-3 2-4z" fill="none" stroke="#2b2b2b" stroke-width="2"/></svg>
      <span>: 0400 555 182</span>
    </li>
    <li>
      <svg viewBox="0 0 28 28" fill="none" stroke="#2b2b2b" stroke-width="1.8"><circle cx="14" cy="15" r="11"/><ellipse cx="14" cy="15" rx="5" ry="11"/><path d="M3 15h22M5 9h18M5 21h18"/></svg>
      <span>: 47 Tarcoola Street</span>
    </li>
    <li class="indent">Brenmore 2899</li>
    <li>
      <svg viewBox="0 0 28 28"><rect x="2" y="7" width="24" height="16" fill="#2b2b2b"/><path d="M2 7l12 9 12-9" fill="none" stroke="#ffd51c" stroke-width="1.5"/></svg>
      <span>: callreardon@mailbox.com</span>
    </li>
  </ul>

  <div class="hero-photo" role="img" aria-label="Photo of a yellow motor grader parked on a dry stubble paddock under blue sky"></div>
  <div class="hero-caption">Earthmoving &amp; Transport</div>

  <div class="tread tread--front" role="img" aria-label="Grey tyre tread band"></div>
</section>

<section class="card card--back">
  <div class="back-photo" role="img" aria-label="Black and white photo of a prime mover towing flat-top trailers loaded with cotton equipment"></div>
  <div class="tread tread--top" role="img" aria-label="Grey tyre tread band"></div>
  <div class="tread tread--bottom" role="img" aria-label="Grey tyre tread band"></div>

  <div class="services services--earth">
    <h2>Earthmoving</h2>
    <ul>
      <li>Road Building &amp; Maintenance</li>
      <li>Poly Pipe Laying</li>
      <li>Clearing fence lines</li>
      <li>Sand &amp; Gravel supplies</li>
    </ul>
  </div>
  <div class="services services--transport">
    <h2>Transport</h2>
    <ul>
      <li>Grain</li>
      <li>Cotton</li>
      <li>Sand &amp; Gravel</li>
      <li>Wool</li>
    </ul>
  </div>
</section>

</body>
</html>
```